Mapping of agricultural parcels

Creation in January 2019 of the VORLANIX company, specialized in capturing, exploiting and distributing aerial images for agriculture. Need to communicate on a brochure to make known the existence of the company and the services and services offered to agricultural laboratories, and farmers and agricultural cooperatives. The brochure should highlight the return on investment (ROI) and the relevance of services for the development of sustainable agriculture. To carry out its missions, the company has expertise in: - piloting drones (operator and remote pilot) - building and distributing maps - in web & mobile development

Target Market(s)

Exploitation and agricultural cooperative Laboratory of Agronomy Industrial in the agri-food sector

Font styles to use
Serif

Colors
00a990
ffffff
5c5c5c

Requirements
Must have
• to present the proposed services to present the advantages for the client to present the mode of operation and the contacts (see website www.plaincrop-example.fr)
Nice to have
• - Sustainable agriculture - Biomass map and Modulation - Return on investment - Clear and simple aspect - Functional and practical aspect put forward
Should not have
• - too much color - complicated (too much to read) - too elegant

```html
<!DOCTYPE html>
<html lang="fr">
<head>
<meta charset="utf-8">
<title>VORLANIX – Brochure cartographie agricole</title>
<link rel="stylesheet" href="https://fonts.googleapis.com/css2?family=Roboto:wght@400;700&family=Roboto+Condensed:wght@700&family=Roboto+Slab:wght@600;700&display=swap">
<style>
  :root {
    --green: #4c9b3a;
    --teal: #00a990;
    --ink: #5c5c5c;
    --paper: #ffffff;
    --bg: #eef0ee;
    --field-1: #7fa56a;
    --field-2: #a9b98d;
    --sky: #c9d6dc;
    --soil: #9c8a72;
  }
  * { box-sizing: border-box; margin: 0; padding: 0; }
  html, body { width: 1200px; height: 800px; overflow: hidden; background: var(--bg); }
  body { font-family: "Roboto", Arial, sans-serif; color: var(--ink); }

  .spread {
    position: absolute; left: 50px; top: 30px;
    width: 1100px; height: 740px;
    display: grid; grid-template-columns: 1fr 1fr;
    box-shadow: 0 12px 40px rgba(0,0,0,.18);
    background: var(--paper);
  }
  .page { position: relative; overflow: hidden; background: var(--paper); }
  .page--left { border-right: 1px solid #e2e2e2; }
  .photo { display: block; }

  /* left page */
  .hero-map {
    height: 270px;
    background: linear-gradient(170deg, var(--sky) 0%, #b9c7b0 30%, var(--field-1) 55%, var(--soil) 100%);
  }
  .banner {
    position: absolute; left: 28px; top: 252px;
    background: var(--green); color: var(--paper);
    font-family: "Roboto Condensed", Arial, sans-serif; font-weight: 700;
    font-size: 26px; letter-spacing: .5px;
    padding: 10px 26px;
  }
  .services { position: absolute; top: 330px; left: 40px; right: 40px; }
  .service { display: grid; grid-template-columns: 96px 1fr; gap: 30px; align-items: center; margin-bottom: 32px; }
  .service__icon {
    width: 96px; height: 96px; background: var(--green);
    display: flex; align-items: center; justify-content: center;
  }
  .service__text { font-size: 13px; line-height: 1.55; }

  /* right page */
  .page--right { display: grid; grid-template-columns: 100px 1fr 1fr; grid-template-rows: 200px 1fr; }
  .top-photo { grid-column: 1 / 3; grid-row: 1; position: relative; background: linear-gradient(180deg, #cfd9d0 0%, #a8bd98 35%, var(--field-1) 100%); }
  .section-head {
    position: absolute; left: 0; top: 0; background: var(--green); color: var(--paper);
    font-family: "Roboto Slab", Georgia, serif; font-weight: 700; font-size: 21px;
    padding: 9px 18px;
  }
  .photo-strip { grid-column: 1; grid-row: 2; display: grid; grid-template-rows: repeat(4, 1fr); gap: 6px; padding-top: 6px; }
  .photo-strip .photo:nth-child(odd) { background: linear-gradient(160deg, var(--field-2), var(--field-1)); }
  .photo-strip .photo:nth-child(even) { background: linear-gradient(200deg, #9bb07c, #5f8a4c); }
  .col { padding: 14px 14px 0; font-size: 11px; line-height: 1.45; }
  .col--mid { grid-column: 2; grid-row: 2; }
  .col--right { grid-column: 3; grid-row: 1 / 3; display: flex; flex-direction: column; padding-top: 16px; }
  .col h3 {
    font-family: "Roboto Slab", Georgia, serif; font-weight: 600;
    color: var(--green); font-size: 12.5px; line-height: 1.3; margin: 10px 0 5px;
  }
  .col ul { padding-left: 14px; }
  .col li { margin-bottom: 2px; }
  .col li::marker { color: var(--teal); }
  .brand { display: flex; align-items: center; justify-content: flex-end; gap: 8px; margin-bottom: 4px; }
  .brand__dot { width: 14px; height: 14px; background: var(--green); }
  .brand__name { font-weight: 700; font-size: 20px; color: var(--green); }
  .web { font-size: 10px; text-align: right; color: var(--teal); }
  .bottom-photo {
    margin: auto -14px 0 -14px; height: 180px;
    background: linear-gradient(180deg, #c8d3d6 0%, #9fb38a 35%, #7ea060 65%, #8c9a5a 100%);
  }
</style>
</head>
<body>
<main class="spread">
  <section class="page page--left">
    <div class="photo hero-map" role="img" aria-label="Photo de champ labouré avec carte multispectrale de modulation superposée et drone en vol"></div>

    <h2 class="banner">CE QUE NOUS FAISONS</h2>

    <div class="services">
      <div class="service">
        <div class="service__icon">
          <svg width="60" height="60" viewBox="0 0 60 60" fill="none" stroke="#fff" stroke-width="3">
            <rect x="22" y="26" width="16" height="8" rx="2"/><line x1="8" y1="22" x2="22" y2="28"/><line x1="52" y1="22" x2="38" y2="28"/>
            <line x1="2" y1="20" x2="16" y2="20"/><line x1="44" y1="20" x2="58" y2="20"/><line x1="30" y1="34" x2="30" y2="44"/>
          </svg>
        </div>
        <p class="service__text">Contribuer au développement d'une agriculture plus raisonnée en développant la surveillance de vos cultures avec l'imagerie aérienne par drones.</p>
      </div>
      <div class="service">
        <div class="service__icon">
          <svg width="60" height="60" viewBox="0 0 60 60" fill="none" stroke="#fff" stroke-width="3">
            <polygon points="6,24 22,18 38,24 54,18 54,52 38,58 22,52 6,58"/>
            <path d="M30 6c-6 0-10 4-10 9 0 7 10 17 10 17s10-10 10-17c0-5-4-9-10-9z" fill="#4c9b3a"/><circle cx="30" cy="15" r="3"/>
          </svg>
        </div>
        <p class="service__text">Cartographier précisément vos parcelles avec l'exploitation technologie RTK pour mesurer et délimiter précisément vos surfaces agricoles.</p>
      </div>
      <div class="service">
        <div class="service__icon">
          <svg width="60" height="60" viewBox="0 0 60 60" fill="none" stroke="#fff" stroke-width="3">
            <path d="M30 54C14 44 12 24 30 6c18 18 16 38 0 48z"/><line x1="30" y1="14" x2="30" y2="56"/>
          </svg>
        </div>
        <p class="service__text">Mesurer vos apports éléments par le modulation déduite de l'observation de vos cultures dans les domaines multi-spectraux et réaliser des économies tout en préservant les ressources naturelles.</p>
      </div>
    </div>
  </section>

  <section class="page page--right">
    <div class="top-photo photo" role="img" aria-label="Photo aérienne de parcelles agricoles vertes">
      <h2 class="section-head">NOS PRESTATIONS</h2>
    </div>
    <div class="photo-strip">
      <div class="photo" role="img" aria-label="Photo de serre agricole"></div>
      <div class="photo" role="img" aria-label="Photo de rangs de cultures"></div>
      <div class="photo" role="img" aria-label="Photo aérienne de champs"></div>
      <div class="photo" role="img" aria-label="Photo de drone au-dessus d'une culture"></div>
    </div>
    <div class="col col--mid">
      <h3>Photographies aériennes de vos parcelles agricoles à différents stades de leur développement</h3>
      <ul>
        <li>Mieux observer vos cultures et repérer les zones à problème</li>
        <li>Conserver une trace de l'évolution de vos parcelles</li>
        <li>Partager vos vues aériennes avec vos conseillers</li>
        <li>Suivre l'historique de vos parcelles</li>
      </ul>
      <h3>Conversion de cartes pour la surveillance de vos cultures (carte de la biomasse, carte de zonage...)</h3>
      <ul>
        <li>Détecter les carences et les stress</li>
        <li>Identifier les zones à problème</li>
      </ul>
      <h3>Relever précisément vos sinistres par la photographie aérienne</h3>
      <ul>
        <li>Identifier et mesurer le périmètre</li>
        <li>Délimiter précisément les zones concernées</li>
        <li>Justifier précisément votre déclaration</li>
      </ul>
    </div>
    <div class="col col--right">
      <div class="brand"><span class="brand__dot"></span><span class="brand__name">VORLANIX</span></div>
      <p class="web">www.plaincrop-example.fr</p>
      <h3>Mise à disposition de carte de préconisation (carte de semis) pour la modulation manuelle ou automatique</h3>
      <ul>
        <li>Limiter vos apports d'intrants sur les zones</li>
        <li>Moduler vos apports en fonction des besoins</li>
        <li>Maîtriser vos coûts</li>
      </ul>
      <h3>Vos cartes avec la distribution sur le cloud avec une application mobile</h3>
      <ul>
        <li>Vos cartes consultables et partageables</li>
        <li>Compatibles avec vos outils de terrain</li>
        <li>Accès simple depuis votre mobile</li>
      </ul>
      <h3>Formation au pilotage de drones et à l'exploitation de l'imagerie aérienne en milieu agricole</h3>
      <ul>
        <li>Bases de la réglementation drone</li>
        <li>Prise en main du drone et du logiciel</li>
        <li>Interprétation des cartes obtenues</li>
        <li>La modulation manuelle et automatique</li>
      </ul>
      <div class="bottom-photo photo" role="img" aria-label="Photo de vallée agricole avec carte de biomasse superposée"></div>
    </div>
  </section>
</main>
</body>
</html>
```